Whole body Cryotherapy Tri fold Brochure

I am looking to do a tri fold brochure for a whole body cryotherapy business called Fernvale Cryotherapy.I do not have imagery but i would like to try to utilize images to support the benefits of Whole body cryotherapy. I will provide the content needed for the different sides. We would like to see blues and whatever would flow with the design. Also the machine that i will be using is called a PELOM and i would like to add that to the side flap of the brochure. I would really like this to be a modern unique twist since this type of treatment is fairly new to the United states.

Target Market(s)

women, men, children, athletes, health , modern medicine , alternative medicine

Industry/Entity Type

Alternative Medicine

Font styles to use
Sans Serif

Requirements
Must have
• Modern design with bold features, big colorful pictures.
Nice to have
• Font styles can be changed as well. Br

```html
<!DOCTYPE html>
<html lang="en">
<head>
<meta charset="utf-8">
<title>Fernvale Cryotherapy Tri-fold Brochure</title>
<link href="https://fonts.googleapis.com/css2?family=Open+Sans:wght@400;600;700;800&display=swap" rel="stylesheet">
<style>
:root{
  --bg:#6b4a2f;
  --blue:#1e6fb8;
  --blue-dark:#16548e;
  --white:#ffffff;
  --ink:#3a3a3a;
  --muted:#6d6d6d;
  --skin:#c9a58c;
}
*{margin:0;padding:0;box-sizing:border-box}
html,body{width:841px;height:1200px;overflow:hidden}
body{background:var(--bg);font-family:'Open Sans',Arial,sans-serif;color:var(--ink);position:relative}
.label{position:absolute;color:var(--white);font-weight:700;font-size:17px}
.sheet{position:absolute;left:44px;width:753px;display:flex;box-shadow:0 2px 8px rgba(0,0,0,.35)}
.sheet.outside{top:58px;height:500px}
.sheet.inside{top:598px;height:510px}
.panel{width:251px;height:100%;position:relative;background:var(--white);overflow:hidden}
.photo{position:absolute}
/* outside flap */
.flap{background:linear-gradient(180deg,#9fb6c9 0%,#5c7e9c 60%,#1e6fb8 100%)}
.flap .photo{inset:0 0 110px 0;background:linear-gradient(180deg,#e8eef3,#a9bccb 55%,#6f8da8)}
.brand{display:flex;align-items:center;gap:8px;font-weight:800;color:var(--white);font-size:17px;line-height:1.05}
.brand .dot{width:22px;height:22px;border-radius:50%;background:var(--white);flex:none}
.flap .brand{position:absolute;left:22px;bottom:34px}
/* back */
.back{padding:18px 18px}
.back h2{color:var(--blue);font-size:15px;text-align:center;margin-bottom:8px}
.back p{font-size:7.5px;line-height:1.45;margin-bottom:7px;text-align:justify;color:var(--muted)}
.badges{display:grid;grid-template-columns:repeat(3,1fr);gap:6px;margin:10px 0 12px}
.badges span{height:22px;border-radius:3px;background:#d9e4ee}
.badges span:nth-child(odd){background:#c6d6e6}
.contact{text-align:center}
.contact h3{color:var(--blue);font-size:15px;margin-bottom:4px}
.contact p{text-align:center;margin-bottom:2px}
/* front */
.front .logo{margin:20px 0 0 26px}
.front .brand{color:var(--blue);font-size:20px}
.front .brand .dot{background:var(--blue);width:28px;height:28px}
.front .tag{position:absolute;left:0;right:0;top:86px;text-align:center;color:var(--blue);font-size:18px;font-weight:600;line-height:1.25}
.front .photo{right:0;top:148px;width:180px;bottom:0;background:linear-gradient(160deg,#f3e7dd,var(--skin) 60%,#8a6a55)}
/* inside */
.inside .panel{padding:16px 16px}
.inside h2{color:var(--blue);font-size:14px;margin-bottom:8px}
.inside h4{font-size:9px;margin:6px 0 3px;color:var(--ink)}
.inside p{font-size:7.3px;line-height:1.45;color:var(--muted);margin-bottom:6px}
.narrow{width:112px}
.info{position:absolute;left:0;right:0;bottom:0;height:150px;background:var(--blue);color:var(--white);padding:12px 16px}
.info h3{font-size:10px;font-weight:700;margin-bottom:6px;line-height:1.3}
.info ul{list-style:none}
.info li{font-size:7.2px;line-height:1.55;padding-left:9px;position:relative}
.info li::before{content:"";position:absolute;left:0;top:4px;width:4px;height:4px;background:var(--white);border-radius:50%}
.p-left .photo{right:0;top:40px;width:120px;height:320px;background:linear-gradient(180deg,#e9edf1,var(--skin) 55%,#7d6452)}
.p-center .photo{left:16px;right:16px;top:120px;height:120px;background:linear-gradient(135deg,#d6dde4,#8fa3b6 60%,#4d6278)}
.p-center .after{margin-top:180px}
.p-right .photo{right:0;top:175px;width:115px;height:185px;background:linear-gradient(180deg,#f4e9df,var(--skin) 60%,#8d6d58)}
</style>
</head>
<body>
<div class="label" style="left:30px;top:14px">Outside flap</div>
<div class="label" style="left:395px;top:14px">Back</div>
<div class="label" style="left:700px;top:14px">Front</div>

<section class="sheet outside">
  <div class="panel flap">
    <div class="photo" role="img" aria-label="Client standing inside a whole body cryotherapy chamber with cold vapour"></div>
    <div class="brand"><span class="dot"></span><span>FERNVALE<br>CRYOTHERAPY</span></div>
  </div>
  <div class="panel back">
    <h2>What is Whole Body Cryotherapy?</h2>
    <p>Whole Body Cryotherapy is a session of cooling exposure that exposes the body to extremely cold air for two to three minutes. This brief, dry cold triggers a natural response that helps the body restore, recover and feel renewed from head to toe.</p>
    <p>During the session, the skin surface cools quickly while the core stays safe. Blood flow moves toward vital organs and returns enriched when you step out, leaving you energized, refreshed and ready for the day ahead.</p>
    <div class="badges" aria-label="Featured in">
      <span></span><span></span><span></span><span></span><span></span><span></span><span></span><span></span><span></span>
    </div>
    <div class="contact">
      <h3>Contact: 555-014-2290</h3>
      <p>48 Harlow Lane, Brookmere</p>
      <p>hello@fernvalecryo.com</p>
      <p>Open daily · walk-ins welcome</p>
    </div>
  </div>
  <div class="panel front">
    <div class="logo brand"><span class="dot"></span><span>FERNVALE<br>CRYOTHERAPY</span></div>
    <div class="tag">FOR A BETTER<br>HEALTHIER YOU</div>
    <div class="photo" role="img" aria-label="Fit woman in athletic wear smiling"></div>
  </div>
</section>

<section class="sheet inside">
  <div class="panel p-left">
    <div class="photo" role="img" aria-label="Woman stretching after a wellness session"></div>
    <h2>Health and Wellness</h2>
    <p class="narrow">Whole Body Cryotherapy can help to ease a range of chronic conditions such as inflammation, joint stiffness, fatigue and poor sleep. Many guests report better mood and more energy after only a few sessions.</p>
    <p class="narrow">Regular visits support the body's own repair process and may work well alongside other care plans for lasting results.</p>
    <div class="info">
      <h3>Additional Benefits For Health And Wellness Include:</h3>
      <ul>
        <li>Eases joint and muscle pain</li>
        <li>Reduces everyday stress levels</li>
        <li>Promotes deeper, restful sleep</li>
        <li>Boosts natural energy levels</li>
        <li>Supports a healthy immune system</li>
        <li>Lifts mood and mental clarity</li>
      </ul>
    </div>
  </div>
  <div class="panel p-center">
    <h2>Recovery and Performance</h2>
    <p>Professional teams and elite athletes use cold therapy to recover faster between training days, reduce soreness and stay at the top of their game.</p>
    <div class="photo" role="img" aria-label="Athlete training outdoors"></div>
    <p class="after">Recovery sessions help tired muscles bounce back and let you train harder, more often, with less downtime.</p>
    <div class="info">
      <h3>Reported benefits of Whole Body Cryotherapy for recovery and performance include:</h3>
      <ul>
        <li>Faster muscle recovery</li>
        <li>Less soreness after workouts</li>
        <li>Improved range of motion</li>
        <li>Reduced swelling</li>
        <li>Fewer rest days needed</li>
        <li>Better endurance overall</li>
      </ul>
    </div>
  </div>
  <div class="panel p-right">
    <h2>Beauty and Anti-Aging</h2>
    <h4>Increased Metabolism and Weight Loss</h4>
    <p>The body works to warm itself after each session, burning extra calories and giving your metabolism a lift that lasts for hours afterward.</p>
    <div class="photo" role="img" aria-label="Woman with glowing skin touching her face"></div>
    <h4>Anti-Aging</h4>
    <p class="narrow">Cold exposure boosts collagen production, tightens the skin and helps reduce the look of fine lines for a fresh glow.</p>
    <div class="info">
      <h3>Additional Benefits:</h3>
      <ul>
        <li>Tighter, firmer, more youthful skin</li>
        <li>Reduced look of cellulite</li>
        <li>Healthier hair and nails</li>
        <li>Calmer, clearer complexion</li>
        <li>Natural, lasting glow</li>
        <li>Improved body confidence</li>
      </ul>
    </div>
  </div>
</section>

<div class="label" style="left:70px;top:1160px">Inside Left</div>
<div class="label" style="left:360px;top:1160px">Inside Center</div>
<div class="label" style="left:640px;top:1160px">Inside Right</div>
</body>
</html>
```